Linen Lantern Co Logo & Van wrap design

BUSINESS NAME IS (Linen Lantern Co)
This is a wrap on a Kestrel Cargolux 2200 High Roof Van I will attach scaled artwork of the van.
This is a new company so we will need a logo design along with the van wrap. The business is a Dry Cleaning and Laundry pickup and delivery service. They will pickup from business and residential customer, clean and return their laundry clean. We are open on colors something that will grab your ATTENTION this will be the only advertising for the business. The customer is open to a full or partial wrap.

THIS INFO should be on wrap
-Free Pickup and Delivery
-Dry Clean
-Laundry
-Wash -Dry Fold
-Household

Phone Number TBD on bottom

```html
<!DOCTYPE html>
<html lang="en">
<head>
<meta charset="utf-8">
<title>Linen Lantern Co – Kestrel Cargolux 2200 Wrap</title>
<link href="https://fonts.googleapis.com/css2?family=Poppins:ital,wght@0,500;0,800;1,500;1,800&display=swap" rel="stylesheet">
<style>
  :root {
    --stage: #1c1c1c;
    --navy: #0b2a8c;
    --navy-deep: #061a5e;
    --royal: #1f6fe0;
    --sky: #cfe6fb;
    --cyan: #12c2ee;
    --cyan-soft: #7fdcf6;
    --yellow: #f7ea12;
    --white: #ffffff;
    --silver: #b9c2cc;
  }
  * { margin: 0; padding: 0; box-sizing: border-box; }
  html, body { width: 1200px; height: 900px; overflow: hidden; background: var(--stage); }
  .canvas { position: relative; width: 1200px; height: 900px; font-family: "Poppins", sans-serif; }
  .wrap-panel { position: absolute; left: 40px; top: 170px; width: 1120px; height: 560px; }
  .wrap-art { position: absolute; inset: 0; }
  .bubbles-art {
    position: absolute; left: 700px; top: 50px; width: 320px; height: 110px;
    border-radius: 160px 160px 40px 40px;
    background: radial-gradient(ellipse at 50% 70%, var(--cyan) 0%, var(--cyan-soft) 60%, rgba(127,220,246,0) 100%);
  }
  .brand-name {
    position: absolute; left: 680px; top: 165px; width: 430px;
    font-weight: 800; font-size: 58px; line-height: 1.02; text-transform: uppercase;
    color: var(--cyan-soft); letter-spacing: 0.5px;
  }
  .mascot-art {
    position: absolute; left: 565px; top: 240px; width: 100px; height: 115px;
    border-radius: 50px 50px 18px 18px;
    background: linear-gradient(160deg, #eef3f8, #9fb2c8);
  }
  .socials { position: absolute; left: 250px; top: 295px; display: flex; gap: 14px; list-style: none; }
  .social { display: flex; flex-direction: column; align-items: center; gap: 4px; }
  .social-dot {
    width: 42px; height: 42px; border-radius: 50%;
    background: radial-gradient(circle at 40% 35%, var(--cyan-soft), var(--cyan));
  }
  .social-name { font-size: 11px; font-weight: 500; color: var(--navy); }
  .offer {
    position: absolute; left: 345px; top: 378px; width: 260px;
    font-weight: 800; font-style: italic; font-size: 33px; line-height: 1.02; text-align: right;
    color: var(--yellow); -webkit-text-stroke: 1.5px var(--navy-deep);
    paint-order: stroke fill; text-shadow: 2px 2px 0 var(--navy-deep);
  }
  .services {
    position: absolute; left: 620px; top: 382px; width: 440px; list-style: none;
    display: grid; grid-template-columns: 215px 215px; row-gap: 8px;
  }
  .services li {
    font-style: italic; font-weight: 500; font-size: 17px; line-height: 22px; color: var(--white);
    letter-spacing: 0.5px; white-space: nowrap;
  }
  .services li::before { content: "•"; margin-right: 10px; font-size: 13px; }
  .url-strip {
    position: absolute; left: 410px; top: 462px; width: 580px; height: 40px;
    background: var(--navy-deep); border-radius: 4px;
  }
  .url {
    position: absolute; left: 420px; top: 459px;
    font-weight: 800; font-size: 28px; color: var(--yellow);
    -webkit-text-stroke: 1px var(--navy-deep); paint-order: stroke fill;
  }
  .phone {
    position: absolute; left: 830px; top: 466px;
    font-weight: 800; font-size: 22px; color: var(--white); letter-spacing: 0.5px;
  }
</style>
</head>
<body>
<div class="canvas">
  <section class="wrap-panel" aria-label="Van side wrap artwork">
    <svg class="wrap-art" viewBox="0 0 1120 560" aria-hidden="true">
      <defs>
        <linearGradient id="leftField" x1="0" y1="0" x2="0.7" y2="1">
          <stop offset="0" stop-color="#2f86ea"/>
          <stop offset="0.35" stop-color="#cfe6fb"/>
          <stop offset="0.7" stop-color="#ffffff"/>
        </linearGradient>
        <radialGradient id="navyGlow" cx="0.62" cy="0.45" r="0.6">
          <stop offset="0" stop-color="#1f5ad0"/>
          <stop offset="1" stop-color="#071f72"/>
        </radialGradient>
      </defs>
      <rect x="0" y="0" width="1120" height="560" rx="60" fill="url(#leftField)"/>
      <path d="M0 0 H420 Q330 120 300 260 L0 260 Z" fill="#1f6fe0" opacity="0.55"/>
      <path d="M520 0 H1060 Q1120 0 1120 60 V500 Q1120 560 1060 560 H560 Q440 300 520 0 Z" fill="url(#navyGlow)"/>
      <path d="M490 0 H520 Q440 300 560 560 H530 Q410 300 490 0 Z" fill="#12c2ee"/>
      <path d="M478 0 H490 Q410 300 530 560 H518 Q396 300 478 0 Z" fill="#b9c2cc"/>
      <path d="M540 440 H1120 V560 H600 Q565 500 540 440 Z" fill="#061a5e" opacity="0.35"/>
    </svg>

    <div class="bubbles-art" role="img" aria-label="Cluster of soap bubbles above the logo"></div>
    <h1 class="brand-name">Linen Lantern Co</h1>
    <div class="mascot-art" role="img" aria-label="Cartoon mascot illustration beside the logo"></div>

    <ul class="socials" aria-label="Social channels">
      <li class="social"><span class="social-dot"></span><span class="social-name">Friendwall</span></li>
      <li class="social"><span class="social-dot"></span><span class="social-name">Snapfeed</span></li>
      <li class="social"><span class="social-dot"></span><span class="social-name">Postline</span></li>
    </ul>

    <p class="offer">FREE PICKUP + DELIVERY</p>
    <ul class="services">
      <li>DRY CLEANING</li>
      <li>WASH-DRY-FOLD</li>
      <li>LAUNDRY PICKUP</li>
      <li>HOUSEHOLD</li>
    </ul>

    <div class="url-strip"></div>
    <p class="url">www.linenlanternco.com</p>
    <p class="phone">PHONE: TBD</p>
  </section>
</div>
</body>
</html>
```